Thyroid treatment trifold brochure

We need a trifold brochure to have on display at other businesses, especially targeted for women ages 35 -65. Highlighting Hair loss, weight gain, lack of answers from Primary care dr. We specialize in hormone balancing with bio-identical hormone replacement. the uploaded file is an example from another clinic that has good info. I would like to also focus on how we are approach therapy different and find answers where other clinics fail. The most effective approach is the right medicine, (naturally dessicated Thyroid medication) and paying attention to symptoms. Most doctors are only trained to look at bloodwork and adjust a synthetic thyroid med. So many women are frustrated by the lack of help available.
Want thicker fuller hair? Check your thyroid!
Thinning Hair, Hairline and Eyebrows? #1 Reason and how to reverse it.
Is your thyroid medication causing hair loss?
• The truth is that levothyroxine itself can cause hair loss independent of whatever dose you are taking.
• It may be the case that you are taking the exact amount of levothyroxine that your body needs to function but you can STILL experience hair loss.
• That's because one of the side effects of levothyroxine is hair loss.
If you aren't seeing improvement in your hair growth after changing your thyroid medication to an naturally desiccated medication, then look to these nutrients:
• Selenium
• Zinc
• Iron
• Vitamin B12
• Biotin
• Choline
These nutrients are necessary for hair growth and if you don't have enough of them your hair will not grow even if your thyroid is stimulating your hair follicles.
Are your thyroid medications working? Here is how to tell
7 Thyroid medications mistakes you don’t want to make
1. You’re on the wrong medication for your body - Synthetic vs. Bio-Identical
2. You don’t take your medication correctly
3. You don’t store your medication properly
4. You don't separate coffee, milk, and your thyroid medication
5. You ignore continued symptoms that should have resolved
6. You use a Doctor that only relies on blood work to diagnose
7. You don’t know if you have glandular vs. cellular hypothyroidism

Thyroid Quiz
In the last few weeks have you:
Felt tired?
Gained Weight?
Felt colder than other people?
Had Constipation?
Had Hair problems?
Had Skin Problems?
Had Nail Problems?
Had a Loss of Appetite?
Had hearing problems?
Had voice problems?
Had speech problems?
Had memory problems?
Had problems with concentration?
Felt giddy of dizzy?
Felt depressed or low?

Yes no

Target Market(s)

women 35-65

Industry/Entity Type

medical clinic

Colors
0094D4
00A9DD
6FCCEA
C7EBF8
E9F6FB

Requirements
Nice to have
• a little quiz or tips on checking for sign's by looking in the mirror

```html
<!DOCTYPE html>
<html lang="en">
<head>
<meta charset="UTF-8">
<title>Lumera Health – Thyroid Trifold</title>
<link href="https://fonts.googleapis.com/css2?family=Poppins:wght@400;500;600;700&family=Varela+Round&display=swap" rel="stylesheet">
<style>
:root{
  --green:#9dba4c;
  --green-dark:#86a63a;
  --grey:#c9c9c9;
  --grey-mid:#a9a9a9;
  --grey-dark:#6f6f6f;
  --panel-light:#ededed;
  --paper:#f4f4f4;
  --ink:#4a4a4a;
  --slate:#8a9aa8;
  --bg:#e6e6e6;
}
*{box-sizing:border-box;margin:0;padding:0}
html,body{width:1200px;height:900px;overflow:hidden;background:var(--bg)}
body{position:relative;font-family:'Poppins',sans-serif;color:var(--ink)}
.sheet{position:absolute;left:20px;width:1160px;height:420px;display:grid;grid-template-columns:repeat(3,1fr);background:var(--paper);box-shadow:0 6px 18px rgba(0,0,0,.12)}
.sheet--outside{top:20px}
.sheet--inside{top:460px}
.panel{position:relative;overflow:hidden;border-right:1px solid rgba(0,0,0,.06)}
.panel:last-child{border-right:none}
.panel__bg{position:absolute;inset:0;width:100%;height:100%}
.panel__content{position:relative;height:100%}
.heading{font-family:'Varela Round','Poppins',sans-serif;color:var(--green);font-weight:700}
.brand{display:flex;align-items:center;gap:8px;font-family:'Poppins',sans-serif;font-weight:600;color:var(--green)}
.brand__dot{width:22px;height:22px;border-radius:50%;background:var(--green)}
.photo{position:absolute}
/* quiz */
.quiz{padding:42px 26px 0}
.quiz .heading{font-size:26px;margin-bottom:10px}
.quiz__intro,.quiz__list li,.quiz__answer{font-size:9.5px;line-height:11.6px;color:#555}
.quiz__list{list-style:none;width:200px}
.quiz__answer{margin-top:8px}
.quiz__toggle{position:absolute;right:26px;top:150px;display:flex;gap:6px}
.quiz__toggle span{width:30px;height:30px;border-radius:50%;background:var(--green);color:#fff;font-size:9px;font-weight:600;display:flex;align-items:center;justify-content:center}
/* contact */
.contact{display:flex;flex-direction:column;align-items:center;padding-top:88px;text-align:center}
.contact .heading{color:var(--slate);font-size:24px;margin-bottom:20px}
.contact__label{font-size:8px;font-weight:600;color:var(--slate);letter-spacing:.3px;text-transform:uppercase}
.contact__value{font-size:10.5px;font-weight:600;color:var(--green);margin:2px 0 14px}
.contact__social{list-style:none;text-align:left}
.contact__social li{display:flex;align-items:center;gap:7px;font-size:10.5px;font-weight:500;color:var(--green);margin-bottom:6px}
.contact__social li::before{content:"";width:10px;height:10px;border-radius:50%;background:var(--grey-dark)}
/* cover */
.cover .brand{position:absolute;top:44px;left:0;right:0;justify-content:center;font-size:22px;color:#fff}
.cover__headline{position:absolute;left:36px;top:170px;font-family:'Poppins',sans-serif;font-weight:700;font-size:20px;line-height:25px;color:#fff}
.cover__sub{position:absolute;left:0;right:0;top:330px;text-align:center;font-size:13px;font-weight:600;line-height:16px;color:#3f3f3f}
/* mistakes */
.mistakes{padding:28px 24px}
.mistakes .brand{font-size:20px;margin-bottom:16px}
.mistakes .heading{font-size:16px;line-height:19px;margin-bottom:6px}
.mistakes__sub{font-family:'Varela Round',sans-serif;font-weight:700;color:var(--green);font-size:11px;line-height:13px;margin-bottom:10px}
.mistakes__list{list-style:none;counter-reset:m}
.mistakes__list li{counter-increment:m;position:relative;padding-left:16px;font-size:9px;line-height:11.5px;color:#4d4d4d;margin-bottom:3px}
.mistakes__list li::before{content:counter(m);position:absolute;left:0;top:-1px;font-weight:700;font-style:italic;color:var(--slate);font-size:11px}
/* nutrients */
.nutrients{padding:26px 26px}
.nutrients__quote{font-family:'Varela Round',sans-serif;font-weight:700;color:var(--green);font-size:14px;line-height:17px;margin-bottom:10px}
.nutrients__list{list-style:none;margin-bottom:8px}
.nutrients__list li{font-size:9.5px;line-height:12.5px;color:#555;padding-left:26px;position:relative}
.nutrients__list li::before{content:"·";position:absolute;left:0}
.nutrients__note{font-size:9px;line-height:11px;font-weight:600;color:var(--slate);text-align:justify}
/* hair loss */
.hairloss{padding:200px 24px 0}
.hairloss .heading{font-size:17px;line-height:20px;margin-bottom:10px}
.hairloss__list{list-style:none}
.hairloss__list li{position:relative;padding-left:16px;font-size:9px;line-height:11px;color:#555;margin-bottom:8px;text-align:justify}
.hairloss__list li::before{content:"·";position:absolute;left:2px}
</style>
</head>
<body>

<section class="sheet sheet--outside" aria-label="Brochure outside">
  <article class="panel">
    <svg class="panel__bg" viewBox="0 0 387 420" preserveAspectRatio="none" aria-hidden="true">
      <rect width="387" height="420" fill="#ededed"/>
      <path d="M110 0 Q190 40 387 32 L387 0 Z" fill="#9dba4c"/>
      <path d="M0 352 Q190 318 387 345 L387 420 L0 420 Z" fill="#9dba4c"/>
    </svg>
    <div class="panel__content quiz">
      <h2 class="heading">Thyroid Quiz</h2>
      <p class="quiz__intro">In the last few weeks have you:</p>
      <ul class="quiz__list">
        <li>Felt tired?</li><li>Gained Weight?</li><li>Felt colder than other people?</li><li>Had Constipation?</li><li>Had Hair problems?</li><li>Had Skin Problems?</li><li>Had Nail Problems?</li><li>Had a Loss of Appetite?</li><li>Had hearing problems?</li><li>Had voice problems?</li><li>Had speech problems?</li><li>Had memory problems?</li><li>Had problems with concentration?</li><li>Felt giddy or dizzy?</li><li>Felt depressed or low?</li>
      </ul>
      <p class="quiz__answer">Yes / No</p>
      <div class="quiz__toggle"><span>YES</span><span>NO</span></div>
      <div class="photo" role="img" aria-label="Illustration of a puzzled woman weighing yes and no answers" style="left:120px;top:340px;width:150px;height:80px;border-radius:75px 75px 0 0;background:linear-gradient(180deg,#f2b6a4,#e98870)"></div>
    </div>
  </article>

  <article class="panel">
    <svg class="panel__bg" viewBox="0 0 387 420" preserveAspectRatio="none" aria-hidden="true">
      <rect width="387" height="420" fill="#efefef"/>
      <path d="M0 0 L387 0 L387 50 Q200 110 0 60 Z" fill="#9dba4c"/>
    </svg>
    <div class="photo" role="img" aria-label="Faint backdrop photo of flowing hair" style="inset:70px 0 0 0;background:linear-gradient(180deg,#ececec,#e4e4e4)"></div>
    <div class="panel__content contact">
      <h2 class="heading">Contact Us</h2>
      <p class="contact__label">Phone numbers</p>
      <p class="contact__value">+1 555 0142 / 0199</p>
      <p class="contact__label">Website</p>
      <p class="contact__value">www.lumerahealth.com</p>
      <p class="contact__label">Address</p>
      <p class="contact__value">YOUR ADDRESS HERE</p>
      <p class="contact__label">Social media</p>
      <ul class="contact__social" style="margin-top:4px">
        <li>facebook.com/lumerahealth</li>
        <li>instagram.com/lumerahealth</li>
        <li>twitter.com/lumerahealth</li>
      </ul>
    </div>
  </article>

  <article class="panel">
    <svg class="panel__bg" viewBox="0 0 387 420" preserveAspectRatio="none" aria-hidden="true">
      <rect width="387" height="420" fill="#a9a9a9"/>
      <path d="M0 120 Q150 80 387 160 L387 300 Q200 340 0 300 Z" fill="#c9c9c9"/>
      <circle cx="200" cy="195" r="118" fill="#9dba4c"/>
    </svg>
    <div class="panel__content cover">
      <div class="brand"><span class="brand__dot"></span>Lumera Health</div>
      <div class="photo" role="img" aria-label="Photo of a woman's long wavy hair with floral hairpins" style="left:92px;top:85px;width:220px;height:220px;border-radius:50%;background:radial-gradient(circle at 55% 45%,#9c7452,#6b4b33 70%)"></div>
      <h1 class="cover__headline">Want thicker<br>fuller hair?<br>Check your<br>thyroid!</h1>
      <p class="cover__sub">Thinning Hair,<br>Hairline and Eyebrows?<br>#1 Reason<br>and how to reverse it.</p>
    </div>
  </article>
</section>

<section class="sheet sheet--inside" aria-label="Brochure inside">
  <article class="panel">
    <svg class="panel__bg" viewBox="0 0 387 420" preserveAspectRatio="none" aria-hidden="true">
      <rect width="387" height="420" fill="#c9c9c9"/>
      <path d="M0 350 Q190 310 387 360 L387 420 L0 420 Z" fill="#a9a9a9"/>
    </svg>
    <div class="panel__content mistakes">
      <div class="brand"><span class="brand__dot"></span>Lumera Health</div>
      <h2 class="heading">Are your thyroid<br>medications working?</h2>
      <p class="mistakes__sub">Here is how to tell – 7 Thyroid medications mistakes you don't want to make</p>
      <ol class="mistakes__list">
        <li>You're on the wrong medication for your body – Synthetic vs. Bio-Identical</li>
        <li>You don't take your medication correctly</li>
        <li>You don't store your medication properly</li>
        <li>You don't separate coffee, milk, and your thyroid medication</li>
        <li>You ignore continued symptoms that should have resolved</li>
        <li>You use a Doctor that only relies on blood work to diagnose</li>
        <li>You don't know if you have glandular vs. cellular hypothyroidism</li>
      </ol>
    </div>
  </article>

  <article class="panel">
    <svg class="panel__bg" viewBox="0 0 387 420" preserveAspectRatio="none" aria-hidden="true">
      <rect width="387" height="420" fill="#efefef"/>
      <path d="M40 420 Q40 320 200 318 Q360 320 387 380 L387 420 Z" fill="#9dba4c"/>
    </svg>
    <div class="photo" role="img" aria-label="Photo of a woman with hair blown across her face" style="left:60px;top:334px;width:280px;height:100px;border-radius:140px 140px 0 0;background:linear-gradient(180deg,#8a7467,#3f3230)"></div>
    <div class="panel__content nutrients">
      <p class="nutrients__quote">If you aren't seeing improvement in your hair growth after changing your thyroid medication to a naturally desiccated medication, then look to these nutrients:</p>
      <ul class="nutrients__list">
        <li>Selenium</li><li>Zinc</li><li>Iron</li><li>Vitamin B12</li><li>Biotin</li><li>Choline</li>
      </ul>
      <p class="nutrients__note">These nutrients are necessary for hair growth and if you don't have enough of them your hair will not grow even if your thyroid is stimulating your hair follicles.</p>
    </div>
  </article>

  <article class="panel">
    <svg class="panel__bg" viewBox="0 0 387 420" preserveAspectRatio="none" aria-hidden="true">
      <rect width="387" height="420" fill="#f4f4f4"/>
      <path d="M0 0 L387 0 L387 150 Q200 200 0 120 Z" fill="#9dba4c"/>
      <path d="M0 150 Q200 230 387 170 L387 230 Q200 260 0 200 Z" fill="#dcdcdc"/>
    </svg>
    <div class="photo" role="img" aria-label="Photo of a woman with long brown hair in a denim jacket outdoors" style="left:40px;top:0;width:347px;height:165px;border-radius:0 0 0 180px;background:linear-gradient(135deg,#5c6b58,#8a7566 60%,#5a7590)"></div>
    <div class="panel__content hairloss">
      <h2 class="heading">Is your thyroid<br>medication causing<br>hair loss?</h2>
      <ul class="hairloss__list">
        <li>The truth is that levothyroxine itself can cause hair loss independent of whatever dose you are taking.</li>
        <li>It may be the case that you are taking the exact amount of levothyroxine that your body needs to function but you can STILL experience hair loss.</li>
        <li>That's because one of the side effects of levothyroxine is hair loss.</li>
      </ul>
    </div>
  </article>
</section>

</body>
</html>
```